Nobody Saw It Coming Podcast Design

I'm starting a new podcast called, "Nobody saw it coming?" It highlights bizarre and often unintentional record holders, wannabe record holders and should be record holders. I'm looking for a design that incorporates the title and appears a little off kilter like the show and stir curiosity. Leaninsstoward some autumn colors; burnt rsd and some type of gold but open to other colors.sPodcast art specs:sCover art must be in the JPEG or PNG file formats and in the RGB color space with a minimum size of 1400 x 1400 pixels and a maximum size of 3000 x 3000 pixelss

```html
<!DOCTYPE html>
<html lang="en">
<head>
<meta charset="utf-8">
<title>Nobody Saw It Coming — Podcast Cover</title>
<link rel="stylesheet" href="https://fonts.googleapis.com/css2?family=League+Spartan:wght@700&display=swap">
<style>
  :root {
    --bg-deep: #241010;
    --bg-warm: #2f1612;
    --tan-orange: #d9843c;
    --bright-orange: #f58d20;
    --burnt-red: #d63a2f;
    --oxblood: #7a1115;
    --gold: #fbc20c;
  }
  html, body {
    margin: 0;
    padding: 0;
    width: 1200px;
    height: 1200px;
    overflow: hidden;
    background: var(--bg-deep);
  }
  .cover {
    display: block;
    width: 1200px;
    height: 1200px;
  }
  .cover__title {
    font-family: "League Spartan", "Futura", sans-serif;
    font-weight: 700;
  }
  .title-word--nobody { fill: var(--tan-orange); }
  .title-word--saw { fill: var(--bright-orange); }
  .title-word--it { fill: var(--burnt-red); }
  .title-word--coming { fill: var(--oxblood); }
  .title-mark { fill: var(--gold); }
</style>
</head>
<body>
<svg class="cover" viewBox="0 0 1200 1200" xmlns="http://www.w3.org/2000/svg" role="img" aria-label="Nobody saw it coming?">
  <defs>
    <radialGradient id="backdrop" cx="50%" cy="45%" r="75%">
      <stop offset="0%" stop-color="var(--bg-warm)"/>
      <stop offset="100%" stop-color="var(--bg-deep)"/>
    </radialGradient>
  </defs>
  <rect class="cover__backdrop" width="1200" height="1200" fill="url(#backdrop)"/>

  <g class="cover__title">
    <text class="title-word title-word--nobody" x="140" y="370" font-size="405" textLength="965" lengthAdjust="spacingAndGlyphs">NOBODY</text>
    <text class="title-word title-word--saw" x="140" y="745" font-size="478" textLength="600" lengthAdjust="spacingAndGlyphs">SAW</text>
    <text class="title-word title-word--it" x="795" y="745" font-size="478" textLength="310" lengthAdjust="spacingAndGlyphs">IT</text>
    <text class="title-word title-word--coming" x="140" y="1115" font-size="470" textLength="850" lengthAdjust="spacingAndGlyphs">COMING</text>
    <text class="title-mark" x="1008" y="1112" font-size="215" textLength="80" lengthAdjust="spacingAndGlyphs">?</text>
  </g>
</svg>
</body>
</html>
```